Millbrook Artisanal & Craft Beer ***

WordPress Website redesign for an existing site https://millbrookogunquit-example.com/ and https://millbrookportsmouth-example.com/ (currently broken). Only one site, We want the Portsmouth site to be the one created. There have been issues with it in the past which caused it to crash and just randomly loose data/not hold the installed code. We want it to look similar to the other site listed as they are one company with two locations. that's why we added both. The Ogt location is for reference only.
Client is a Pizza and craft beer Restaurant/Foodservice establishment in Portsmouth, NH USA. wanting to have a more secure site that is visually appealing, efficient, and easy for the staff to go in and adjust menu items periodically
both the Reservation and the Gift card tabs/button will link to external sites (tablyx.com, payvenly.com, with restaurant specific info) so they will need to be for design purpose only.

Target Market(s)

Restaurant Dining, Consumers

Industry/Entity Type

foodservice, Restaurant

Coding

Coded - Design and coding required

Number of Pages Required

5+ page

Colors

Designer to choose colors to be used in the design.

Requirements
Must have
• Menu that is easily accessible by customers on their phones from a QR code. Gift cards and online sales (need to be separate for companies) I like that the current site is one page that is scrollable with clicks to sections and it can be easily viewed n mobile phone. It should have sections: menu, reservations (link), order take out (link), buy gift cards (link), work here (with application form), Events/Private Parties, Data collection boilerplate legal statement? Must be easily editable by my staff so they can change menu items Needs to use our logo and branding better
Nice to have
• Can it collect emails for advertising purposes? Can this automatically go into a system that my staff can use?

```html
<!DOCTYPE html>
<html lang="en">
<head>
<meta charset="utf-8">
<title>Millbrook Artisanal Pizza & Craft Beer – Portsmouth</title>
<link href="https://fonts.googleapis.com/css2?family=Dosis:wght@400;500;600;700&family=Open+Sans:wght@400;600;700&family=Montserrat:wght@600;700&display=swap" rel="stylesheet">
<style>
:root{
  --cream:#e8e1d9;
  --red:#d64032;
  --brown:#4a2c1d;
  --ink:#4a3a30;
  --muted:#6a5d54;
  --wood-dark:#2a1c14;
  --field:#f4efe9;
  --white:#ffffff;
}
*{margin:0;padding:0;box-sizing:border-box}
html,body{width:1200px;height:3691px;overflow:hidden}
body{background:var(--cream);font-family:'Open Sans',sans-serif;color:var(--ink);position:relative}
.abs{position:absolute}
.center{text-align:center}
a{color:inherit;text-decoration:none}

.site-header{position:absolute;top:0;left:0;width:1200px;height:125px;background:var(--cream)}
.brand{position:absolute;left:75px;top:34px;width:258px}
.brand-name{font-family:'Montserrat',sans-serif;font-weight:700;font-size:29px;color:var(--brown);letter-spacing:1px;line-height:1}
.brand-tag{margin-top:6px;background:var(--red);color:var(--white);font-family:'Dosis',sans-serif;font-weight:600;font-size:15px;text-align:center;padding:3px 0}
.main-nav{position:absolute;right:75px;top:58px;display:flex;gap:29px;font-family:'Dosis',sans-serif;font-weight:700;font-size:15px;color:var(--brown);text-transform:uppercase}

.hours-band{position:absolute;top:125px;left:0;width:1200px;height:110px;background:var(--red);color:var(--white);font-family:'Dosis',sans-serif;font-weight:600;font-size:24px;line-height:36px;text-align:center;padding-top:18px}

.section-title{position:absolute;left:0;width:1200px;text-align:center;font-family:'Dosis',sans-serif;color:var(--ink)}
.rule{position:absolute;height:9px;background:var(--brown)}
.photo{position:absolute}
.label{position:absolute;text-align:center;font-family:'Dosis',sans-serif;font-weight:600;font-size:17px;letter-spacing:9px;color:var(--brown);text-transform:uppercase}
.note{position:absolute;text-align:center;font-size:15px;color:var(--muted)}
.btn{position:absolute;background:var(--red);color:var(--white);font-weight:700;font-size:13px;text-align:center;line-height:37px;text-transform:uppercase}

.footer{position:absolute;top:2620px;left:0;width:1200px;height:980px;background:linear-gradient(180deg,#52392b,#3f2a1f 60%,#4a3224)}
.f-head{position:absolute;width:330px;left:805px;text-align:center;font-family:'Dosis',sans-serif;font-weight:600;font-size:27px;color:var(--white);text-transform:uppercase}
.f-text{position:absolute;width:330px;left:805px;text-align:center;font-size:16px;line-height:30px;color:var(--white)}

.apply{position:absolute;left:66px;top:2690px;width:697px;height:563px;background:var(--cream);padding:26px 30px}
.apply h3{font-family:'Dosis',sans-serif;font-weight:600;font-size:27px;color:var(--brown);text-transform:uppercase}
.apply .lead{font-size:14px;color:var(--muted);margin:4px 0 16px}
.apply .row{display:flex;gap:18px;margin-bottom:12px}
.apply .col{flex:1}
.apply .lbl{font-family:'Dosis',sans-serif;font-weight:600;font-size:14px;letter-spacing:2px;color:var(--brown);text-transform:uppercase;margin-bottom:4px}
.apply .box{height:36px;background:var(--field);border:1px solid #c9bcb0}
.apply .area{height:84px}
.apply .submit{display:inline-block;margin-top:6px;width:200px;background:var(--red);color:var(--white);font-weight:700;font-size:13px;line-height:37px;text-align:center;text-transform:uppercase}

.signup{position:absolute;left:66px;top:3337px;width:1067px;height:175px;border:1px dashed #8a7566}
.signup h3{position:absolute;top:34px;width:100%;text-align:center;font-family:'Montserrat',sans-serif;font-size:20px;color:var(--white);letter-spacing:1px}
.signup p{position:absolute;top:76px;width:100%;text-align:center;font-family:'Montserrat',sans-serif;font-size:11px;color:var(--cream);letter-spacing:3px}
.signup .field{position:absolute;left:204px;top:117px;width:523px;height:32px;background:var(--wood-dark);color:#bba99b;font-family:'Montserrat',sans-serif;font-size:12px;letter-spacing:2px;line-height:32px;padding-left:12px}
.signup .go{position:absolute;left:727px;top:117px;width:130px;height:32px;background:var(--cream);color:var(--brown);font-family:'Montserrat',sans-serif;font-size:12px;letter-spacing:2px;line-height:32px;text-align:center}
.legal{position:absolute;left:66px;top:3530px;width:1067px;text-align:center;font-size:12px;line-height:20px;color:#b8a595}

.footer-bottom{position:absolute;top:3600px;left:0;width:1200px;height:91px;background:var(--wood-dark);color:#6e5a4c;font-size:12px;padding:24px 66px;line-height:22px}
</style>
</head>
<body>

<header class="site-header">
  <div class="brand">
    <div class="brand-name">MILLBROOK</div>
    <div class="brand-tag">Artisanal Pizza &amp; Craft Beer</div>
  </div>
  <nav class="main-nav">
    <a href="#menu">Menu &#711;</a><a href="#directions">Directions</a><a href="#reserve">Online Reservation</a><a href="#takeout">Order Take Out</a><a href="#call">603-555-0148</a>
  </nav>
</header>

<div class="hours-band">• OPEN WEDNESDAY-FRIDAY • 5-9PM • SATURDAY • 12-9PM • SUNDAY • 12-8PM • CLOSED MONDAYS<br>&amp; TUESDAYS, THANKSGIVING, CHRISTMAS EVE &amp; CHRISTMAS DAY!! 603.555.0148</div>

<h1 class="section-title" style="top:310px;font-size:34px;font-weight:500">Artisanal Pizza &amp; Craft Beer in Downtown Portsmouth</h1>

<div class="rule" style="left:66px;top:405px;width:514px"></div>
<div class="photo" role="img" aria-label="Close-up of a lobster pizza with stone-oven crust" style="left:66px;top:425px;width:514px;height:300px;background:linear-gradient(135deg,#6b3a22,#c98a55 45%,#e6c08f 60%,#3a2a22)"></div>
<div class="label" style="left:66px;top:741px;width:514px">• Order Take Out •</div>
<div class="note" style="left:66px;top:775px;width:514px">Call 603-555-0148 or order online</div>
<div class="abs center" style="left:66px;top:805px;width:514px;font-weight:700;font-size:24px;color:#f0555a">Order Online &nbsp;<span style="display:inline-block;width:30px;height:30px;border-radius:50%;background:#f0555a;vertical-align:-6px"></span>&nbsp; <span style="color:var(--wood-dark)">TakeoutLoop</span></div>

<div class="rule" style="left:620px;top:405px;width:513px"></div>
<div class="photo" role="img" aria-label="Wooden restaurant sign hanging outside the entrance" style="left:620px;top:425px;width:513px;height:300px;background:linear-gradient(160deg,#e8e6e0,#b87a55 45%,#5a4a40 70%,#8a6a4c)"></div>
<div class="note" style="left:620px;top:738px;width:513px;font-weight:600;color:var(--brown);line-height:30px">• Reservations available through Tablyx. Reservations for 7 or<br>more please call to make your reservation</div>

<h2 class="section-title" style="top:940px;font-size:38px;font-weight:500">ARTISANAL PIZZA &amp; CRAFT BEER</h2>
<div class="rule" style="left:66px;top:1038px;width:1067px"></div>
<div class="photo" role="img" aria-label="Stone-baked pizza with basil and sun-dried tomatoes" style="left:66px;top:1060px;width:1067px;height:615px;background:radial-gradient(ellipse at 55% 50%,#d9b48a 0%,#b07a4e 45%,#3a2c26 80%)"></div>
<div class="label" style="left:66px;top:1692px;width:1067px">• Artisanal Pizza &amp; Craft Beer •</div>
<div class="note" style="left:66px;top:1726px;width:1067px">Handcrafted from the finest ingredients.</div>
<a class="btn" href="#menu" style="left:67px;top:1763px;width:1065px">View Menu</a>

<div class="abs center" style="left:459px;top:1950px;width:282px;height:46px;line-height:46px;background:var(--red);font-family:'Montserrat',sans-serif;font-weight:700;font-size:19px;color:var(--white);letter-spacing:2px">MILLBROOK</div>
<div class="abs center" style="left:459px;top:2018px;width:282px;font-family:'Dosis',sans-serif;font-size:13px;color:var(--brown)">Artisanal Pizza &amp; Craft Beer</div>
<div class="abs center" style="left:66px;top:2049px;width:1067px;font-weight:600;font-size:16px;color:var(--brown)">Serving artisanal stone oven pizza and hand selected local and imported craft beers since 2012.</div>
<div class="abs center" style="left:66px;top:2081px;width:1067px;font-size:15.5px;line-height:30px;color:var(--muted)">Enjoy chef created pizza on our home made dough and savory apps and entrees inspired by the freshest ingredients – from our house<br>made sausage to fresh Maine Lobster and local produce – all cooked in our stone oven and thoughtfully paired with craft beer for<br>optimum flavor combinations.</div>

<div class="rule" style="left:66px;top:2208px;width:327px"></div>
<div class="photo" role="img" aria-label="Patio set for a private party with red umbrellas" style="left:66px;top:2228px;width:327px;height:190px;background:linear-gradient(180deg,#7a9a5a,#c9553f 45%,#5c6a3a)"></div>
<div class="label" style="left:66px;top:2437px;width:327px">• Events •</div>
<div class="note" style="left:66px;top:2472px;width:327px">Private parties &amp; group dining</div>
<a class="btn" href="#events" style="left:67px;top:2507px;width:325px">Plan An Event</a>

<div class="rule" style="left:436px;top:2208px;width:327px"></div>
<div class="photo" role="img" aria-label="Pizza with tomatoes on a dark stone" style="left:436px;top:2228px;width:327px;height:190px;background:radial-gradient(ellipse at 50% 55%,#d8b083,#9a6a44 55%,#2e2622)"></div>
<div class="label" style="left:436px;top:2437px;width:327px">• Portsmouth, NH •</div>
<div class="note" style="left:436px;top:2472px;width:327px">52 Kiln Lane, Portsmouth, NH</div>
<a class="btn" href="#menu" style="left:437px;top:2507px;width:325px">View Menu</a>

<div class="rule" style="left:807px;top:2208px;width:326px"></div>
<div class="photo" role="img" aria-label="Bar shelves stocked with bottles" style="left:807px;top:2228px;width:326px;height:190px;background:linear-gradient(90deg,#3a2e28,#8a7a6c 50%,#c9b59a)"></div>
<div class="label" style="left:807px;top:2437px;width:326px">• Gift Cards •</div>
<div class="note" style="left:807px;top:2472px;width:326px">Any Location. Never Expire.</div>
<a class="btn" href="#gift" style="left:808px;top:2507px;width:324px">Buy Gift Cards</a>

<footer class="footer"></footer>

<form class="apply" id="work-here">
  <h3>Work Here</h3>
  <div class="lead">Join our Portsmouth team. Tell us a little about yourself.</div>
  <div class="row"><div class="col"><div class="lbl">Full Name</div><div class="box"></div></div><div class="col"><div class="lbl">Email</div><div class="box"></div></div></div>
  <div class="row"><div class="col"><div class="lbl">Phone</div><div class="box"></div></div><div class="col"><div class="lbl">Position</div><div class="box"></div></div></div>
  <div class="row"><div class="col"><div class="lbl">Availability</div><div class="box"></div></div><div class="col"><div class="lbl">Resume</div><div class="box"></div></div></div>
  <div class="row"><div class="col"><div class="lbl">Experience</div><div class="box area"></div></div></div>
  <div class="submit">Send Application</div>
</form>

<div class="f-head" style="top:2693px">Hours</div>
<div class="f-text" style="top:2735px">• Open Wednesday-Friday 5-9PM •<br>Saturday • 12-9pm • Sunday • 12-8pm<br>CLOSED MONDAYS &amp; TUESDAYS,<br>THANKSGIVING, CHRISTMAS EVE &amp;<br>CHRISTMAS DAY</div>
<div class="f-head" style="top:2918px">Visit Us</div>
<div class="f-text" style="top:2962px">52 Kiln Lane, Portsmouth, NH</div>
<div class="f-head" style="top:3028px">Contact Us</div>
<div class="f-text" style="top:3072px">603-555-0148<br><b>EMPLOYMENT:</b><br>hello@millbrook-example.com</div>
<div class="f-head" style="top:3200px">Stay Connected</div>
<div class="f-text" style="top:3253px;font-size:22px;font-weight:600">Friendpage &nbsp;&nbsp; TripNotes</div>

<div class="signup">
  <h3>WELCOME. MAY WE TAKE YOUR EMAIL?</h3>
  <p>NEWS • UPDATES • SPECIALS • SERVED TO YOUR INBOX • AS ORDERED</p>
  <div class="field">EMAIL ADDRESS</div>
  <div class="go">SUBSCRIBE</div>
</div>
<div class="legal">We collect your email only to send news and specials. We never sell your data; unsubscribe any time.<br>Applications are kept private and used only for hiring at our Portsmouth location.</div>

<div class="footer-bottom"><b>EMPLOYMENT:</b> hello@millbrook-example.com<br>Privacy &amp; Data Collection Policy • Terms of Use<br>© 2017 Millbrook Pizza And Beer.</div>

</body>
</html>
```